Wordpress website design needed for website re-launch of established lawn care company (Design mu...

We are a gardening company and are separating and re-launching the lawn care part of the company. We already have a non-wordpress website which includes a lawn care section and therefore contains all the content needed for the new website. We essentially need to take that content (over 6 pages) and re-create it into a new, modern and visually appealing design in our new Wordpress website. We use Veko and therefore the new design must be built and be compatible with the Veko theme. However, I am not looking to use a pre-built Veko layout or any template offered by Marrow Studio. I could easily do that myself. I'm looking for a bespoke design.

The pages of our current website that need to be re-designed within Veko are:
http://www.brambleworth.co.uk/lawncare/4593693096
http://www.brambleworth.co.uk/lawnfertilisers/4593712410
http://www.brambleworth.co.uk/lawnaeration/4593746736
http://www.brambleworth.co.uk/lawnscarification/4593747084
http://www.brambleworth.co.uk/lawntreatments/4593757226
http://www.brambleworth.co.uk/lawncarepackages/4593712492

Our Wordpress site is already set up with Hostara with the domain www.brambleworthlawns.co.uk and as I say, uses the Veko theme. I am not sure how you will deliver your designs but it must be using or compatible with Veko.

Target Market(s)

Homeowners ages 30+

Industry/Entity Type

Gardener

Font styles to use
Sans Serif

Colors
a64599
9bcb3c

Requirements
Must have
• The new site must still use our existing company colours - purple and green. Have a look on www.brambleworth.co.uk to get the right colours.
• Must be mobile responsive
Nice to have
• We want a fresh and modern new look for our new lawn care website.
• I have also attached a picture of our van and lawn care flyers so you can see what our current branding and style looks like in case it helps with your design.
Should not have
• Please don't just submit pre-designed templates that bear no relevance to my brief or requirements above. I could very easily go and install a pre-designed template and plug my content in but that's not what I'm looking for. Submissions should take into consideration my existing content, my brand colours and my logo as a minimum.

```html
<!DOCTYPE html>
<html lang="en">
<head>
<meta charset="utf-8">
<title>Brambleworth Gardening Services – Lawn Care</title>
<link href="https://fonts.googleapis.com/css2?family=Roboto:wght@400;500;700&display=swap" rel="stylesheet">
<style>
:root{
  --purple:#7d2181;
  --purple-deep:#6a1a70;
  --green:#3bb54a;
  --green-dark:#1f7a34;
  --grass:#4aa23a;
  --text:#333;
  --grey-band:#f3f3f3;
  --soil:#5b3418;
  --soil-dark:#3f2210;
  --white:#fff;
}
*{margin:0;padding:0;box-sizing:border-box}
html,body{width:1200px;height:4055px;overflow:hidden}
body{position:relative;font-family:'Roboto',Arial,sans-serif;color:var(--text);background:var(--white)}
.abs{position:absolute}
.nav{position:absolute;top:22px;left:0;width:1200px;height:20px;z-index:5}
.nav a{position:absolute;font-size:15px;color:#2b2b2b;text-decoration:none;font-weight:500;white-space:nowrap;transform:translateX(-50%)}
.nav a.active{color:var(--green)}
.nav .marker{position:absolute;left:514px;top:-20px;width:30px;height:6px;transform:translateX(-50%)}
.hero{position:absolute;top:0;left:0;width:1200px;height:740px}
.brand{position:absolute;left:192px;top:100px;display:flex;align-items:center;gap:12px;z-index:4}
.brand .dot{width:34px;height:34px;border-radius:50%;background:var(--green)}
.brand .name{font-size:34px;font-weight:500;color:#4a2a12;line-height:1}
.hero-title{position:absolute;top:342px;left:0;width:1200px;text-align:center;font-size:40px;font-weight:500;color:var(--white);z-index:4}
h2.section-title{position:absolute;color:var(--purple);font-weight:500;font-size:34px;line-height:38px}
p.copy{font-size:13.5px;line-height:23px;color:#3a3a3a;margin-bottom:12px}
.intro-copy{position:absolute;left:87px;top:736px;width:515px}
.photo-circle{position:absolute;left:638px;top:636px;width:470px;height:470px;border-radius:50%;background:var(--white);box-shadow:0 6px 18px rgba(0,0,0,.12);padding:16px;z-index:3}
.photo-circle div{width:100%;height:100%;border-radius:50%;background:radial-gradient(circle at 40% 35%,#6fd13a,#2f8a1e 75%)}
.ph{position:absolute}
.pkg-copy{position:absolute;left:603px;top:1279px;width:510px}
.btn-green{position:absolute;left:600px;top:1397px;width:148px;height:38px;border-radius:19px;background:var(--green);color:var(--white);font-size:12px;font-weight:700;display:flex;align-items:center;justify-content:center;box-shadow:0 3px 0 #2a8a36}
.grey-band{position:absolute;top:1558px;left:0;width:1200px;height:552px;background:var(--grey-band)}
.treat-copy{position:absolute;left:85px;top:1763px;width:520px}
.card{position:absolute;overflow:hidden}
.card .label{position:absolute;bottom:34px;left:0;width:100%;text-align:center;color:var(--white);font-size:18px;font-weight:500;line-height:21px}
.card.big .label{font-size:22px;line-height:26px;bottom:30px}
.arrow-btn{position:absolute;width:38px;height:38px;border-radius:50%;display:flex;align-items:center;justify-content:center;color:var(--white);font-size:14px}
.contact-box{position:absolute;left:110px;top:2751px;width:353px;height:490px;background:var(--green);padding:0 33px}
.contact-box h3{margin-top:52px;font-size:33px;font-weight:500;color:var(--white);margin-bottom:10px}
.field{width:284px;height:36px;background:var(--white);margin-bottom:8px;font-size:12px;color:#888;padding:11px 17px}
.field.msg{height:118px}
.submit{width:284px;height:42px;border-radius:21px;background:var(--purple);color:var(--white);font-weight:700;font-size:13px;display:flex;align-items:center;justify-content:center;margin-top:4px}
.analysis-copy{position:absolute;left:540px;top:2906px;width:520px}
.contact-line{font-size:14px;color:var(--green);font-weight:500;display:flex;align-items:center;gap:8px;height:24px}
.contact-line svg{width:12px;height:12px}
.footer{position:absolute;left:0;top:3340px;width:1200px;height:715px;background:var(--soil)}
.foot-brand{position:absolute;left:142px;top:3690px;display:flex;align-items:center;gap:14px}
.foot-brand .dot{width:40px;height:40px;border-radius:50%;background:#8cc63f}
.foot-brand .name{font-size:40px;font-weight:500;color:var(--white)}
.foot-col h4{font-size:23px;font-weight:500;color:var(--white);margin-bottom:6px}
.foot-col a{display:block;font-size:14px;line-height:25px;color:var(--white);text-decoration:none}
.foot-col p{font-size:13.5px;line-height:20px;color:var(--white)}
.foot-col .fl{display:flex;align-items:center;gap:8px;font-size:13.5px;color:var(--white);line-height:24px}
.socials{display:flex;gap:8px;margin-top:10px}
.socials span{width:24px;height:24px;border-radius:50%;display:block}
.foot-rule{position:absolute;left:87px;top:4006px;width:1026px;height:1px;background:rgba(255,255,255,.15)}
.copyright{position:absolute;left:0;top:4020px;width:1200px;text-align:center;font-size:13.5px;color:var(--white)}
.to-top{position:absolute;left:1122px;top:3977px;width:40px;height:40px;border-radius:50%;background:var(--green);display:flex;align-items:center;justify-content:center}
</style>
</head>
<body>

<nav class="nav">
  <svg class="marker" viewBox="0 0 30 6"><path d="M2 1l4 4 4-4M12 1l4 4 4-4M22 1l4 4 4-4" stroke="#3bb54a" stroke-width="2" fill="none"/></svg>
  <a style="left:173px">Home</a>
  <a style="left:248px">About</a>
  <a style="left:375px">Residential Services</a>
  <a class="active" style="left:515px">Lawncare</a>
  <a style="left:661px">Grounds Maintenance</a>
  <a style="left:824px">Garden Advice</a>
  <a style="left:932px">Gallery</a>
  <a style="left:1018px">Contact</a>
</nav>

<svg class="hero" viewBox="0 0 1200 740" aria-hidden="false">
  <defs>
    <linearGradient id="heroPhoto" x1="0" y1="0" x2="1" y2="1">
      <stop offset="0" stop-color="#3f8f2e"/>
      <stop offset=".5" stop-color="#5aa83a"/>
      <stop offset="1" stop-color="#2f6e22"/>
    </linearGradient>
  </defs>
  <path role="img" aria-label="Photo of a lawn mower cutting a striped green lawn beside a garden path" fill="url(#heroPhoto)"
    d="M0,150 C150,300 360,240 560,150 C700,88 820,55 960,58 C1100,62 1200,140 1200,200 L1200,590 C1060,640 880,580 700,510 C520,440 360,420 200,470 C100,505 30,545 0,575 Z"/>
  <path fill="var(--purple)" d="M0,128 C120,260 360,255 560,150 C680,90 760,68 830,64 C740,92 650,140 560,190 C380,292 140,300 0,205 Z"/>
  <path fill="#0c9a4a" d="M480,455 C700,480 950,600 1200,540 L1200,620 C1000,670 780,590 560,505 Z"/>
  <path fill="var(--purple)" d="M0,575 C150,470 350,430 560,480 C800,545 1000,650 1200,580 L1200,625 C1000,700 780,615 560,540 C360,478 160,520 0,610 Z"/>
  <path fill="var(--purple)" d="M1000,640 C1100,640 1170,620 1200,600 L1200,690 C1150,710 1080,720 1000,720 Z" opacity="0"/>
</svg>

<div class="brand"><span class="dot"></span><span class="name">Brambleworth</span></div>
<h1 class="hero-title">Expert Lawn Treatment Service</h1>

<h2 class="section-title" style="left:87px;top:648px">Passionate about<br>Lawn Care</h2>
<div class="intro-copy">
  <p class="copy">As expert gardeners, we are passionate about horticulture and working to bring out the very best in your garden. When we work in your garden, we look at it and treat it with the same care and attention as if it were our own, before handing it back for you to enjoy. Our passion doesn't end with just trees and shrubs, though. Your grass is as much of a living, breathing plant as your shrubs and we, therefore, utilise our expert horticultural knowledge to ensure your lawn thrives and reaches its fullest potential.</p>
  <p class="copy">Lawn care isn't just about applying a fertiliser. It's about really understanding your lawn and being able to use extensive knowledge and experience to diagnose and treat issues. It, therefore, stands to reason that you should employ an expert to bring out the best in your lawn which is why we at Brambleworth Gardening Services have created a superior lawn care service that will keep your lawn looking lush, green and healthy all year round.</p>
</div>
<div class="photo-circle"><div role="img" aria-label="Close-up photo of a green mower over freshly cut grass"></div></div>

<div class="ph" role="img" aria-label="Photo of sunlit grass" style="left:0;top:1247px;width:249px;height:159px;background:linear-gradient(135deg,#d9e88a,#6ab33a 60%,#2f7d22)"></div>
<div class="ph" role="img" aria-label="Photo of pink coneflowers" style="left:126px;top:1176px;width:249px;height:186px;background:linear-gradient(160deg,#8fb84a,#c85a8e 55%,#5c8a2a)"></div>
<div class="ph" role="img" aria-label="Photo of leafy garden shrub" style="left:288px;top:1260px;width:249px;height:184px;background:linear-gradient(140deg,#2e5a1e,#6b9a3e 55%,#24451a)"></div>

<h2 class="section-title" style="left:603px;top:1235px">Lawn Care Packages</h2>
<div class="pkg-copy">
  <p class="copy">Our lawn care treatments can be purchased individually or as part of one of our specially created Lawn Care Packages.</p>
  <p class="copy">These can be paid for on a pay-as-you-go basis, or you can spread the cost evenly over the course of a year with our Monthly Direct Debit Payment Plan.</p>
</div>
<div class="btn-green">FIND OUT MORE</div>

<div class="grey-band"></div>
<h2 class="section-title" style="left:85px;top:1704px">Lawn Treatments</h2>
<div class="treat-copy">
  <p class="copy">As gardeners and horticulturalists we knew what we wanted out of a lawn care product and so spent a great deal of time collaborating with a top agronomist and former premiership-football sports turf consultant, to make sure we selected the very best fertilisers and treatments out there on the market. It will come as no surprise that our highly specialised, organic products are not available to the general public, as they are reserved for use by professionals on some of the most prestigious greens in the world. But now you can benefit from the same specialist treatments and couple with the expert horticultural knowledge of us at Brambleworth Gardening Services, create the healthiest, lushest and greenest of lawns.</p>
</div>
<div class="ph" role="img" aria-label="Photo of a large striped lawn being mown" style="left:764px;top:1619px;width:310px;height:409px;background:linear-gradient(180deg,#1f5a34,#3a8a3a 45%,#5fa644)"></div>
<div class="ph" role="img" aria-label="Photo of dewy grass blades" style="left:665px;top:1762px;width:198px;height:295px;background:linear-gradient(180deg,#b7d96a,#5aa532 55%,#2f6f1e)"></div>

<div class="card" role="img" aria-label="Photo of a fertiliser spreader on a lawn" style="left:88px;top:2233px;width:224px;height:321px;background:linear-gradient(180deg,#6aa34a,#2e6a2a)"><div class="label">Spring<br>Treatment</div></div>
<div class="card big" role="img" aria-label="Photo of a curved garden path through a lawn" style="left:321px;top:2200px;width:320px;height:380px;background:linear-gradient(180deg,#4f7f3a,#5fae3c 55%,#2f7a22)"><div class="label">Early Summer<br>Treatment</div></div>
<div class="card" role="img" aria-label="Photo of a striped back-garden lawn" style="left:649px;top:2233px;width:224px;height:321px;background:linear-gradient(180deg,#8a8f85,#5faa35 50%,#2f7a22)"><div class="label">Late Summer<br>Treatment</div></div>
<div class="card" role="img" aria-label="Photo of a spreader applying autumn feed" style="left:885px;top:2233px;width:224px;height:321px;background:linear-gradient(180deg,#7f95a8,#4e8a3a 55%,#2e6a2a)"><div class="label">Autumn<br>Treatment</div></div>

<div class="arrow-btn" style="left:557px;top:2625px;background:#d7d7d7">&#8249;</div>
<div class="arrow-btn" style="left:603px;top:2625px;background:var(--green)">&#8250;</div>

<div class="contact-box">
  <h3>Contact Us</h3>
  <div class="field">Name*</div>
  <div class="field">Telephone*</div>
  <div class="field">Email*</div>
  <div class="field">Email*</div>
  <div class="field msg">Message*</div>
  <div class="submit">SUBMIT</div>
</div>

<h2 class="section-title" style="left:537px;top:2857px">Lawn Care Analysis</h2>
<div class="analysis-copy">
  <p class="copy">No two lawns are the same, and the needs of one might be very different to the needs of another. In order to assess those needs and offer you our lawn care recommendations, we will need to meet with you and perform an analysis of your lawn. We can then take you through the different options available and provide you with our quote.</p>
  <p class="copy">In order to arrange this, please send us an email, give us a call or complete the adjacent form and we will get in touch.</p>
  <div class="contact-line" style="margin-top:14px"><svg viewBox="0 0 12 12"><path d="M2.5 1l2 2.5-1 1.2a7 7 0 0 0 3.8 3.8l1.2-1 2.5 2-1 1.5C5 11 1 7 1 2.5z" fill="#3bb54a"/></svg>01632 960418</div>
  <div class="contact-line"><svg viewBox="0 0 12 12"><rect x="1" y="2.5" width="10" height="7" fill="#3bb54a"/><path d="M1 3l5 3.5L11 3" stroke="#fff" fill="none"/></svg>enquiries@brambleworth.co.uk</div>
</div>

<div class="footer"></div>
<svg class="abs" style="left:0;top:3330px" width="1200" height="300" viewBox="0 0 1200 300" role="img" aria-label="Illustration of soil mound with tall grass growing on the right">
  <defs>
    <linearGradient id="grassFill" x1="0" y1="0" x2="0" y2="1">
      <stop offset="0" stop-color="#7fc44a"/>
      <stop offset="1" stop-color="#2e7d22"/>
    </linearGradient>
  </defs>
  <rect width="1200" height="300" fill="#fff"/>
  <path d="M560,240 C650,120 800,40 1200,20 L1200,300 L560,300 Z" fill="url(#grassFill)"/>
  <path d="M0,300 L0,150 C80,120 150,60 250,50 C380,40 480,170 650,220 C800,260 980,180 1200,200 L1200,300 Z" fill="var(--soil-dark)"/>
  <path d="M0,300 L0,175 C90,140 160,85 250,75 C380,65 480,195 650,245 C800,285 980,205 1200,225 L1200,300 Z" fill="var(--soil)"/>
</svg>

<div class="foot-brand"><span class="dot"></span><span class="name">Brambleworth</span></div>

<div class="foot-col abs" style="left:504px;top:3686px">
  <h4>Useful Links</h4>
  <a>About</a><a>Residential Services</a><a>Commercial Services</a><a>Lawn Care</a><a>Garden Advice</a><a>Gallery</a><a>Testimonials</a><a>Contact</a><a>Terms &amp; Conditions</a>
</div>

<div class="foot-col abs" style="left:795px;top:3682px;width:290px">
  <h4>Contact us for a Quote</h4>
  <p>Whether it be for a one-off job or for regular garden maintenance, contact Owen for a quote.</p>
  <div class="fl" style="margin-top:4px"><svg width="11" height="11" viewBox="0 0 12 12"><path d="M2.5 1l2 2.5-1 1.2a7 7 0 0 0 3.8 3.8l1.2-1 2.5 2-1 1.5C5 11 1 7 1 2.5z" fill="#3bb54a"/></svg>01632 960418</div>
  <div class="fl"><svg width="11" height="11" viewBox="0 0 12 12"><path d="M2.5 1l2 2.5-1 1.2a7 7 0 0 0 3.8 3.8l1.2-1 2.5 2-1 1.5C5 11 1 7 1 2.5z" fill="#3bb54a"/></svg>enquiries@brambleworth.co.uk</div>
  <div class="socials"><span style="background:#3b5998"></span><span style="background:#1da1f2"></span><span style="background:#dd4b39"></span><span style="background:#2a4a8a"></span></div>
</div>

<div class="foot-rule"></div>
<div class="to-top"><svg width="12" height="8" viewBox="0 0 12 8"><path d="M1 7l5-5 5 5" stroke="#fff" stroke-width="2" fill="none"/></svg></div>
<div class="copyright">© Copyright Brambleworth Gardening Services Ltd ®</div>

</body>
</html>
```